2021 IT Training Presentation Deck Refresh

Copper Lantern is an IT education services firm. We teach IT industry standards and technologies. We are in need of an updated training presentation deck that factors in a fresh take for:

1) Agenda/Table of Contents
2) Chapter Topic Summary
2) Chapter Introduction and Learning Objectives
3) Chapter Recaps
4) Important Point/Pro Tip emphasis
5) Warning Message
6) Mini Quiz layout
7) Lab Exercise Introduction
7) Deck Close Out

Incorporating the official Copper Lantern colour palette for materials that will likely be used in self-paced/online recorded versions of courses.

Target Market(s)

IT

Industry/Entity Type

Computer Training

Requirements
Nice to have
• placeholder sections for images of IT workers in an office or by a computer

```html
<!DOCTYPE html>
<html lang="en">
<head>
<meta charset="utf-8">
<title>Copper Lantern – Training Deck Layouts</title>
<link rel="stylesheet" href="https://fonts.googleapis.com/css2?family=Noto+Sans:wght@400;700&display=swap">
<style>
:root{
  --page:#c8c9cb;
  --paper:#ffffff;
  --navy:#23368e;
  --sky:#7ab9e8;
  --ink:#111318;
  --body:#1d1f24;
  --brand:#2b3d8f;
}
*{margin:0;padding:0;box-sizing:border-box}
html,body{width:1200px;height:4193px;overflow:hidden;background:var(--page)}
body{position:relative;font-family:"Noto Sans",sans-serif;color:var(--body)}
.slide{position:absolute;left:98px;width:1024px;height:768px;background:var(--paper);overflow:hidden}
.slide--quiz{top:91px}
.slide--recap{top:897px}
.slide--lab{top:1698px}
.slide--warning{top:2510px;background:linear-gradient(160deg,#dce9f7 0%,#b9d3ef 45%,#9fc2ea 100%)}
.slide--summary{top:3326px}
.header-band{position:absolute;left:464px;top:0;width:560px;height:111px;z-index:3}
.slide-title{position:absolute;right:33px;top:44px;z-index:4;color:#fff;font-weight:700;font-size:32px;letter-spacing:.5px;line-height:46px;text-transform:uppercase}
.brand{position:absolute;display:flex;align-items:center;gap:12px;color:var(--brand);font-size:34px;font-weight:400;line-height:40px;z-index:2}
.brand-dot{width:22px;height:22px;border-radius:50%;background:var(--brand)}
.photo{position:absolute}
.photo--classroom{left:37px;top:223px;width:355px;height:464px;background:linear-gradient(160deg,#dfe9f2,#9fb4c8 60%,#6d7d8c)}
.photo--pair{left:519px;top:111px;width:505px;height:657px;background:linear-gradient(170deg,#eef0ef,#c9c4bd 55%,#8e96a6)}
.photo--team{left:503px;top:164px;width:264px;height:308px;background:linear-gradient(160deg,#e8ecee,#8d8ea6 60%,#5b4f6d);z-index:2}
.photo--student{left:553px;top:212px;width:440px;height:505px;background:linear-gradient(170deg,#eef1f3,#c6a98f 45%,#3f6e78)}
.photo--silhouette{left:488px;top:16px;width:536px;height:752px;background:linear-gradient(150deg,#3a5fa8,#13286b 50%,#0a1646)}
.photo--group{left:0;top:181px;width:529px;height:511px;background:linear-gradient(160deg,#e2ddd3,#9a7a62 50%,#3c3d48)}
.qa{position:absolute;left:431px;width:560px}
.qa h3{font-size:17px;font-weight:700;color:var(--ink);text-transform:uppercase;line-height:24px;margin-bottom:6px}
.qa p{font-size:16px;line-height:24px}
.qa--1{top:215px}.qa--2{top:386px}.qa--3{top:563px}
.copy{position:absolute;width:410px}
.copy h2{font-size:29px;font-weight:700;color:var(--ink);line-height:42px;text-transform:uppercase;margin-bottom:52px}
.copy p{font-size:17px;line-height:26px;margin-bottom:22px}
.copy--recap{left:57px;top:218px}
.copy--recap h2{margin-bottom:46px}
.copy--lab{left:73px;top:220px}
.copy--lab h2,.copy--warning h2{margin-bottom:28px}
.copy--warning{left:73px;top:220px}
.copy--summary{left:573px;top:226px}
.copy--summary h2{margin-bottom:36px}
</style>
</head>
<body>

<section class="slide slide--quiz">
  <div class="brand" style="left:67px;top:112px"><span class="brand-dot"></span>Copper Lantern</div>
  <svg class="header-band" viewBox="0 0 560 111" aria-hidden="true"><polygon points="4,0 560,0 560,16 10,16" fill="var(--sky)"/><polygon points="12,26 560,26 560,111 51,111" fill="var(--navy)"/></svg>
  <h1 class="slide-title">Mini Quiz Layout</h1>
  <div class="photo photo--classroom" role="img" aria-label="Photo: instructor at a whiteboard teaching a class of students"></div>
  <div class="qa qa--1"><h3>Sed ut perspiciatis unde omnis iste natus</h3><p>Ut enim ad minima veniam, quis nostrum exercitat ionem ullam corporis suscipit laboriosam, nisi ut aliquid ex ea commodi consequatur? Quis autem vel eum iure reprehenderit qui in ea voluptate velit esse quam nihil molestiae consequatur, vel illum qui dolorem eum fugiat</p></div>
  <div class="qa qa--2"><h3>But I must explain to you how all this mistaken</h3><p>No one rejects, dislikes, or avoids pleasure itself, because it is pleasure, but because those who do not know how to pursue pleasure rationally encounter consequences that are extremely painful. Nor again is there anyone who loves or pursues.</p></div>
  <div class="qa qa--3"><h3>At vero eos et accusamus et iusto odio dignissimos</h3><p>Nam libero tempore, cum soluta nobis est eligendi optio cumque nihil impedit quo minus id quod maxime placeat facere possimus, omnis voluptas assumenda est, omnis dolor repellendus. Temporibus autem quibusdam et aut officiis debitis aut rerum</p></div>
</section>

<section class="slide slide--recap">
  <div class="brand" style="left:57px;top:141px"><span class="brand-dot"></span>Copper Lantern</div>
  <svg class="header-band" viewBox="0 0 560 111" aria-hidden="true"><polygon points="4,0 560,0 560,16 10,16" fill="var(--sky)"/><polygon points="12,26 560,26 560,111 51,111" fill="var(--navy)"/></svg>
  <h1 class="slide-title" style="right:39px">Recaps</h1>
  <div class="copy copy--recap"><h2>Lorem ipsum is simply dummy text of the</h2><p>Sed ut perspiciatis unde omnis iste natus error sit voluptatem accusantium doloremque laudantium, totam rem aperiam, eaque ipsa quae ab illo inventore veritatis et quasi architecto beatae vitae dicta sunt explicabo. Nemo enim ipsam volupta tem quia voluptas sit aspernatur aut odit aut fugit, sed quia consequuntur magni dolores eos qui ratione voluptatem sequi nesciunt. Neque porro quisquam est, qui dolorem ipsum quia dolor sit amet, consectetur, adipisci velit, sed quia non numquam eius modi tempora incidunt ut labore et dolore magnam aliquam quaerat voluptatem.</p></div>
  <div class="photo photo--pair" role="img" aria-label="Photo: two smiling students reviewing printed notes together"></div>
</section>

<section class="slide slide--lab">
  <div class="brand" style="left:67px;top:113px"><span class="brand-dot"></span>Copper Lantern</div>
  <svg class="header-band" viewBox="0 0 560 111" aria-hidden="true"><polygon points="4,0 560,0 560,16 10,16" fill="var(--sky)"/><polygon points="12,26 560,26 560,111 51,111" fill="var(--navy)"/></svg>
  <h1 class="slide-title">Lab Exercise Introduction</h1>
  <div class="copy copy--lab"><h2>Sed ut perspiciatis unde omnis iste</h2><p>Ut enim ad minima veniam, quis nostrum exercitationem ullam corporis suscipit laboriosam, nisi ut aliquid ex ea commodi consequatur? Quis autem vel eum iure reprehenderit qui in ea voluptate velit esse quam nihil molestiae consequatur, vel illum qui dolorem eum fugiat</p><p>But I must explain to you how all this mistaken idea of denouncing pleasure and praising pain was born and I will give you a complete account of the system, and expound the actual teachings of the great explorer of the truth, the master-builder of human happiness. No one rejects, dislike</p></div>
  <div class="photo photo--team" role="img" aria-label="Photo: group of students working together at a laptop"></div>
  <div class="photo photo--student" role="img" aria-label="Photo: smiling student with glasses in a classroom"></div>
</section>

<section class="slide slide--warning">
  <div class="photo photo--silhouette" role="img" aria-label="Image: silhouette of a thinking person overlaid with digital interface graphics"></div>
  <div class="brand" style="left:67px;top:113px"><span class="brand-dot"></span>Copper Lantern</div>
  <svg class="header-band" viewBox="0 0 560 111" aria-hidden="true"><polygon points="4,0 560,0 560,16 10,16" fill="var(--sky)"/><polygon points="12,26 560,26 560,111 51,111" fill="var(--navy)"/></svg>
  <h1 class="slide-title">Warning Message</h1>
  <div class="copy copy--warning"><h2>Sed ut perspiciatis unde omnis iste</h2><p>Ut enim ad minima veniam, quis nostrum exercitationem ullam corporis suscipit laboriosam, nisi ut aliquid ex ea commodi consequatur? Quis autem vel eum iure reprehenderit qui in ea voluptate velit esse quam nihil molestiae consequatur, vel illum qui dolorem eum fugiat</p><p>But I must explain to you how all this mistaken idea of denouncing pleasure and praising pain was born and I will give you a complete account of the system, and expound the actual teachings of the great explorer of the truth, the master-builder of human happiness. No one rejects, dislike</p></div>
</section>

<section class="slide slide--summary">
  <div class="brand" style="left:16px;top:89px"><span class="brand-dot"></span>Copper Lantern</div>
  <svg class="header-band" viewBox="0 0 560 111" aria-hidden="true"><polygon points="4,0 560,0 560,16 10,16" fill="var(--sky)"/><polygon points="12,26 560,26 560,111 51,111" fill="var(--navy)"/></svg>
  <h1 class="slide-title" style="right:28px">Topic Summary</h1>
  <div class="photo photo--group" role="img" aria-label="Photo: team of colleagues gathered around a laptop in an office"></div>
  <div class="copy copy--summary"><h2>Introduction and learning objectives</h2><p>Sed ut perspiciatis unde omnis iste natus error sit voluptatem accusantium doloremque laudantium, totam rem aperiam, eaque ipsa quae ab illo inventore veritatis et quasi architecto beatae vitae dicta sunt explicabo. Nemo enim ipsam volupta tem quia voluptas sit aspernatur aut odit aut fugit, sed quia consequuntur magni dolores eos qui ratione voluptatem sequi nesciunt. Neque porro quisquam est, qui dolorem ipsum quia dolor sit amet, consectetur, adipisci velit, sed quia non numquam eius modi tempora incidunt ut labore et dolore magnam aliquam quaerat voluptatem.</p></div>
</section>

</body>
</html>
```